Website for premium health insurance and concierge medicine

This is a brand new website for Brask Insurance Services that specializes in Health Insurance and Concierge Medicine for high net-worth and affluent individuals and families. Through this website, clients will be able to learn about products and services, submit applications, and complete self enrollment forms. The website needs to have a premium look & feel that will appeal to a discerning high net-worth individual.

I’m looking for 4 pages in total to begin with. I’m also looking for a designer who will be interested in continuing to build out this new site further over the next few months.

The headline for each page is listed below:

Page 1: HOME PAGE
“Premium Healthcare | Bespoke Concierge Services | Absolute Peace of Mind.”

Page 2: HEALTH INSURANCE
“Premium Healthcare | Elevated.”

Page 3: CONCIERGE MEDICINE
“Personalized Medicine | At-Home Concierge Care | Your Private Physician, 24/7.”

Page 4: DENTAL & VISION
“Your Smile | Your Vision | Perfected.”

Here are several links to existing websites that can be used as design inspiration:

https://vantromhealth.com
https://www.pelvix.org/specialties-services/other-programs-services/concierge-medicine
https://wardelmdnx.com

More generally speaking, I like a clean, modern, dutch style of websites. Here’s an unrelated site that has a good design:

https://www.morvathis.com

Here are a few additional phrases and keywords that will help inspire the design:

Premium Health Insurance
Executive Health Insurance
Concierge Medicine
24/7 access dedicated concierge team
Integrative Concierge Care

I will upload logo files below, here are the font & colors information:

Font: Trajan Pro Bold
Colors:
Blue: hex code: 0071BD, Rgb code: 0, 113, 189  cmyk code: 87,53,0,0
Gray: hex code: #666666, Rgb code: 102,102,102 cmyk code: 60,51,51,20

```html
<!DOCTYPE html>
<html lang="en">
<head>
<meta charset="utf-8">
<title>Brask Insurance Services</title>
<link href="https://fonts.googleapis.com/css2?family=Cinzel:wght@600;700&family=Montserrat:wght@500;600;700&family=Roboto:wght@400;500&display=swap" rel="stylesheet">
<style>
:root{
  --blue:#0071bd;
  --blue-deep:#0a55a8;
  --navy:#0b1a3a;
  --navy-mid:#0f3470;
  --gray:#666666;
  --ink:#1d1d1f;
  --line:#d9dde3;
  --white:#ffffff;
  --head:'Cinzel',serif;
  --sans:'Montserrat',sans-serif;
  --body:'Roboto',sans-serif;
}
*{box-sizing:border-box;margin:0;padding:0}
html,body{width:1200px;height:4317px;overflow:hidden}
body{position:relative;background:var(--white);font-family:var(--body);color:var(--gray)}
.abs{position:absolute}
.btn{position:absolute;display:flex;align-items:center;justify-content:center;border-radius:22px;background:var(--blue-deep);color:var(--white);font-family:var(--sans);font-weight:700;font-size:11px;letter-spacing:.4px;text-transform:uppercase}
.btn.outline{background:transparent;border:2px solid var(--white)}

/* header */
.site-header{position:absolute;left:0;top:0;width:1200px;height:106px;background:#f3f6fa;border-top:3px solid var(--blue-deep)}
.brand{position:absolute;left:172px;top:30px;white-space:nowrap;font-family:var(--head);font-weight:700;font-size:21px;line-height:24px;color:var(--blue-deep)}
.brand-dot{position:absolute;left:146px;top:35px;width:16px;height:16px;border-radius:50%;background:var(--blue-deep)}
.call{position:absolute;left:664px;top:20px;font-family:var(--sans);font-weight:700;font-size:16px;color:var(--ink);display:flex;align-items:center;gap:8px}
.call span{color:var(--blue-deep)}
.nav{position:absolute;top:73px;font-family:var(--sans);font-weight:500;font-size:13px;color:var(--ink);text-transform:uppercase;white-space:nowrap}
.nav.active::after{content:"";position:absolute;left:0;top:22px;width:60px;height:2px;background:var(--blue-deep)}

/* hero */
.hero{position:absolute;left:0;top:106px;width:1200px;height:566px;background:radial-gradient(ellipse at 85% 70%,#1d56b8 0%,#123b84 35%,var(--navy) 80%);overflow:hidden}
.hero-art{position:absolute;left:30px;top:54px;width:448px;height:468px;border-radius:45% 45% 50% 50%;background:radial-gradient(circle at 50% 40%,#3f8fe8 0%,#1b5bbf 45%,rgba(11,26,58,0) 75%)}
.hero-title{position:absolute;left:501px;top:138px;white-space:nowrap;font-family:var(--head);font-weight:700;font-size:35px;line-height:45px;color:var(--white)}
.hero-title .accent{color:#3d8ef0}
.arrow{position:absolute;width:34px;height:34px;border:2px solid var(--white);border-radius:50%;display:flex;align-items:center;justify-content:center}

/* welcome */
.rule{position:absolute;height:2px;width:92px;background:linear-gradient(90deg,transparent,#555,transparent)}
.center-title{position:absolute;left:0;width:1200px;text-align:center;font-family:var(--head);font-weight:700}
.intro{position:absolute;left:184px;top:870px;width:830px;text-align:justify;text-align-last:center;font-size:15px;line-height:27.5px;color:var(--gray)}

/* feature band */
.band{position:absolute;left:0;top:1150px;width:1200px;height:246px}
.feature{position:absolute;top:1225px;width:190px;text-align:center;color:var(--white);font-family:var(--body);font-weight:500;font-size:16px;line-height:21px}
.feature svg{display:block;margin:0 auto 20px}
.feature-rule{position:absolute;top:1210px;width:1px;height:170px;background:rgba(255,255,255,.18)}

/* products */
.product-img{position:absolute;width:481px;height:501px}
.product-title{position:absolute;font-family:var(--sans);font-weight:500;font-size:31px;color:var(--ink);text-transform:uppercase;white-space:nowrap}
.product-sub{position:absolute;font-family:var(--body);font-size:18px;line-height:27px;color:var(--blue-deep);white-space:nowrap}
.product-text{position:absolute;width:376px;font-size:13.5px;line-height:24.2px;text-align:justify;color:var(--gray)}

/* contact */
.contact{position:absolute;left:0;top:3278px;width:1200px;height:700px}
.field{position:absolute;background:var(--white);border:1px solid #c8d3e2;font-size:16px;color:#444;padding:18px 21px 0}

/* footer */
.f-head{position:absolute;top:4006px;font-family:var(--sans);font-weight:700;font-size:17px;color:var(--ink)}
.f-text{position:absolute;font-size:13px;line-height:19.5px;color:#333}
.social{position:absolute;top:4247px;width:30px;height:30px;border-radius:50%;background:var(--blue-deep)}
</style>
</head>
<body>

<header class="site-header">
  <div class="brand-dot"></div>
  <div class="brand">Brask Insurance<br>Services</div>
  <div class="call">
    <svg width="26" height="26" viewBox="0 0 24 24" fill="none" stroke="#0a55a8" stroke-width="2"><path d="M5 3h4l2 5-2.5 1.5a11 11 0 0 0 6 6L16 13l5 2v4a2 2 0 0 1-2 2A17 17 0 0 1 3 5a2 2 0 0 1 2-2z"/></svg>
    <div><span>Call Us :</span> +1 888 888 8888</div>
  </div>
  <div class="btn" style="left:940px;top:14px;width:114px;height:40px">Apply Now</div>
  <div class="nav active" style="left:468px">Home</div>
  <div class="nav" style="left:551px">Health Insurance</div>
  <div class="nav" style="left:734px">Concierge Medicine</div>
  <div class="nav" style="left:932px">Dental &amp; Vision</div>
</header>

<section class="hero">
  <div class="hero-art" role="img" aria-label="Glowing blue protective shield illustration"></div>
  <h1 class="hero-title">Premium Healthcare<br><span class="accent">Bespoke Concierge Services</span><br>Absolute Peace of Mind</h1>
  <div class="btn" style="left:498px;top:304px;width:136px;height:41px;background:var(--blue-deep)">Apply Now</div>
  <div class="btn outline" style="left:643px;top:304px;width:136px;height:41px">Get Started</div>
  <div class="arrow" style="left:1118px;top:276px"><svg width="12" height="12" viewBox="0 0 12 12" fill="none" stroke="#fff" stroke-width="2"><path d="M4 1l5 5-5 5"/></svg></div>
  <div class="arrow" style="left:1118px;top:324px"><svg width="12" height="12" viewBox="0 0 12 12" fill="none" stroke="#fff" stroke-width="2"><path d="M8 1L3 6l5 5"/></svg></div>
  <svg class="abs" style="left:0;top:440px" width="1200" height="126" viewBox="0 0 1200 126">
    <path d="M0 126 C250 122 480 70 600 28 C720 70 950 122 1200 126 Z" fill="#fff"/>
    <path d="M0 125 C250 121 480 69 600 27 C720 69 950 121 1200 125" fill="none" stroke="#1f6ee0" stroke-width="4"/>
  </svg>
</section>

<div class="rule" style="left:553px;top:723px"></div>
<h2 class="center-title" style="top:745px;font-size:40px;line-height:48px;color:var(--blue-deep)">Welcome to<br><span style="color:#3a3a3a">Brask Insurance Services</span></h2>
<p class="intro">"Sed ut perspiciatis unde omnis iste natus error sit voluptatem accusantium doloremque laudantium, totam rem aperiam, eaque ipsa quae ab illo inventore veritatis et quasi architecto beatae vitae dicta sunt explicabo. Nemo enim ipsam voluptatem quia voluptas sit aspernatur aut odit aut fugit, sed quia consequuntur magni dolores eos qui ratione voluptatem sequi nesciunt. Neque porro quisquam est, qui dolorem ipsum quia dolor sit amet, consectetur, adipisci velit, sed quia non numquam eius modi tempora incidunt ut labore et dolore magnam aliquam quaerat voluptatem ad minima veniam, quis nostrum exercitationem ullam corporis sid ex ea commodi is autem vel eum iure reprehende</p>
<div class="btn" style="left:541px;top:1062px;width:138px;height:40px">Read More</div>

<svg class="band" viewBox="0 0 1200 246" preserveAspectRatio="none">
  <defs><linearGradient id="bandFill" x1="0" y1="0" x2="1" y2="1"><stop offset="0" stop-color="#0f3d8a"/><stop offset="1" stop-color="#0b1a3a"/></linearGradient></defs>
  <path d="M0 52 Q600 -30 1200 46 L1200 246 L0 246 Z" fill="url(#bandFill)"/>
  <path d="M0 40 Q160 20 310 12 Q140 26 0 56 Z" fill="#1a63c8"/>
</svg>
<div class="feature-rule" style="left:297px"></div>
<div class="feature-rule" style="left:488px"></div>
<div class="feature-rule" style="left:694px"></div>
<div class="feature-rule" style="left:922px"></div>
<div class="feature" style="left:113px">
  <svg width="48" height="48" viewBox="0 0 24 24" fill="none" stroke="#fff" stroke-width="1.4"><path d="M16 3l5 5L9 20H4v-5z"/><path d="M13 6l5 5"/></svg>Premium Health<br>Insurance</div>
<div class="feature" style="left:297px">
  <svg width="48" height="48" viewBox="0 0 24 24" fill="none" stroke="#fff" stroke-width="1.4"><path d="M12 20s-8-5-8-11a4.5 4.5 0 0 1 8-2.8A4.5 4.5 0 0 1 20 9c0 6-8 11-8 11z"/></svg>Executive Health<br>Insurance</div>
<div class="feature" style="left:497px">
  <svg width="56" height="48" viewBox="0 0 28 24" fill="none" stroke="#fff" stroke-width="1.4"><circle cx="14" cy="8" r="3.5"/><circle cx="6" cy="10" r="2.6"/><circle cx="22" cy="10" r="2.6"/><path d="M8 20a6 6 0 0 1 12 0z"/><path d="M2 20a4 4 0 0 1 6-3.4M26 20a4 4 0 0 0-6-3.4"/></svg>Concierge Medicine</div>
<div class="feature" style="left:713px">
  <svg width="48" height="48" viewBox="0 0 24 24" fill="none" stroke="#fff" stroke-width="1.4"><path d="M5 3h4l2 5-2.5 1.5a11 11 0 0 0 6 6L16 13l5 2v4a2 2 0 0 1-2 2A17 17 0 0 1 3 5a2 2 0 0 1 2-2z"/></svg>24/7 access dedicated<br>concierge team</div>
<div class="feature" style="left:907px">
  <svg width="48" height="48" viewBox="0 0 24 24" fill="none" stroke="#fff" stroke-width="1.4"><circle cx="12" cy="12" r="3"/><path d="M12 2l2 2.5 3-.8.8 3L20.5 8 19.7 11 22 12l-2.3 1 .8 3-2.7 1.3-.8 3-3-.8L12 22l-2-2.5-3 .8-.8-3L3.5 16l.8-3L2 12l2.3-1-.8-3 2.7-1.3.8-3 3 .8z"/></svg>Integrative<br>Concierge Care</div>

<div class="rule" style="left:553px;top:1487px"></div>
<h2 class="center-title" style="top:1508px;font-size:40px;color:var(--blue-deep)">Products &amp; <span style="color:#3a3a3a">Services</span></h2>

<div class="product-img" role="img" aria-label="Doctor with a tablet consulting a patient" style="left:144px;top:1624px;background:linear-gradient(135deg,#e9e3dc,#b9c3cc 60%,#8a9aa8);clip-path:ellipse(100% 90% at 0% 50%)"></div>
<h3 class="product-title" style="left:677px;top:1716px">Health Insurance</h3>
<p class="product-sub" style="left:677px;top:1766px">Premium Healthcare | Elevated</p>
<p class="product-text" style="left:679px;top:1811px">Sed ut perspiciatis unde omnis iste natus error sit voluptatem accusantium doloremque laudantium, totam rem aperiam, eaque ipsa quae ab illo inventore veritatis et quasi architecto beatae vitae dicta sunt explicabo enim ipsam voluptatem quia voluptas sit aspernatur aut odit aut fugit, sed quia consequuntur magni dolores eos qui ratione</p>
<div class="btn" style="left:679px;top:1984px;width:137px;height:40px">Read More</div>

<div class="product-img" role="img" aria-label="Physician visiting a senior couple at home" style="left:573px;top:2162px;background:linear-gradient(135deg,#c8b8a4,#8fa0b8 50%,#dcdfe4);clip-path:ellipse(100% 90% at 100% 50%)"></div>
<h3 class="product-title" style="left:141px;top:2242px">Concierge Medicine</h3>
<p class="product-sub" style="left:142px;top:2290px">Personalized Medicine | At-Home Concierge Care<br>Your Private Physician, 24/7</p>
<p class="product-text" style="left:144px;top:2361px">Sed ut perspiciatis unde omnis iste natus error sit voluptatem accusantium doloremque laudantium, totam rem aperiam, eaque ipsa quae ab illo inventore veritatis et quasi architecto beatae vitae dicta sunt explicabo enim ipsam voluptatem quia voluptas sit aspernatur aut odit aut fugit, sed quia consequuntur magni dolores eos qui ratione</p>
<div class="btn" style="left:144px;top:2534px;width:138px;height:40px">Read More</div>

<div class="product-img" role="img" aria-label="Dentist examining a smiling patient" style="left:144px;top:2698px;background:linear-gradient(135deg,#9cc2e6,#e8d6cc 55%,#f1ece8);clip-path:ellipse(100% 90% at 0% 50%)"></div>
<h3 class="product-title" style="left:677px;top:2791px">Dental &amp; Vision</h3>
<p class="product-sub" style="left:677px;top:2839px">Your Smile | Your Vision | Perfected</p>
<p class="product-text" style="left:679px;top:2886px">Sed ut perspiciatis unde omnis iste natus error sit voluptatem accusantium doloremque laudantium, totam rem aperiam, eaque ipsa quae ab illo inventore veritatis et quasi architecto beatae vitae dicta sunt explicabo enim ipsam voluptatem quia voluptas sit aspernatur aut odit aut fugit, sed quia consequuntur magni dolores eos qui ratione</p>
<div class="btn" style="left:679px;top:3057px;width:137px;height:40px">Read More</div>

<svg class="contact" viewBox="0 0 1200 700">
  <defs><linearGradient id="contactFill" x1="0" y1="0" x2="0" y2="1"><stop offset="0" stop-color="#1760c0"/><stop offset="1" stop-color="#1a58a8"/></linearGradient></defs>
  <path d="M0 60 Q600 -40 1200 60 L1200 500 L600 686 L0 500 Z" fill="url(#contactFill)"/>
  <path d="M0 40 Q300 8 560 4 Q260 20 0 72 Z M1200 40 Q900 8 640 4 Q940 20 1200 72 Z" fill="#0f4fa8"/>
  <path d="M280 592 L600 690 L920 592" fill="none" stroke="#0b2a6a" stroke-width="5"/>
</svg>
<div class="rule" style="left:553px;top:3401px;background:linear-gradient(90deg,transparent,#fff,transparent)"></div>
<h2 class="center-title" style="top:3422px;font-size:40px;color:var(--white)">Contact Us</h2>
<div class="field" style="left:233px;top:3511px;width:361px;height:52px">First Name</div>
<div class="field" style="left:605px;top:3511px;width:361px;height:52px">Last Name</div>
<div class="field" style="left:233px;top:3576px;width:361px;height:52px">Email address</div>
<div class="field" style="left:605px;top:3576px;width:361px;height:52px">Phone Number</div>
<div class="field" style="left:233px;top:3640px;width:733px;height:116px">Message</div>
<div class="btn outline" style="left:530px;top:3778px;width:140px;height:43px;background:var(--blue-deep)">Submit</div>

<h4 class="f-head" style="left:168px">Sign up for the newsletter</h4>
<p class="f-text" style="left:168px;top:4042px;width:320px">Subscribe to our newsletter to be the first to find out about new models, exclusive events and other information relating to Brask Insurance.</p>
<div class="abs" style="left:168px;top:4121px;width:283px;height:41px;border:1px solid #b9c0ca;border-radius:21px;font-size:12px;color:#333;padding:13px 0 0 30px">Email Address</div>
<div class="btn" style="left:352px;top:4121px;width:99px;height:41px">Sign Up</div>

<h4 class="f-head" style="left:577px">Contact Us</h4>
<svg class="abs" style="left:577px;top:4046px" width="16" height="14" viewBox="0 0 16 14" fill="#0a55a8"><path d="M0 2l5-2 6 2 5-2v12l-5 2-6-2-5 2z"/></svg>
<p class="f-text" style="left:611px;top:4042px;width:180px;line-height:17px">123,Nemo enim ipsam volu ptatem quia voluptas</p>
<svg class="abs" style="left:577px;top:4096px" width="14" height="14" viewBox="0 0 24 24" fill="#0a55a8"><path d="M5 3h4l2 5-2.5 1.5a11 11 0 0 0 6 6L16 13l5 2v4a2 2 0 0 1-2 2A17 17 0 0 1 3 5a2 2 0 0 1 2-2z"/></svg>
<p class="f-text" style="left:615px;top:4093px">+1 888 888 8888</p>
<svg class="abs" style="left:577px;top:4131px" width="14" height="11" viewBox="0 0 14 11" fill="#0a55a8"><path d="M0 0h14v11H0z"/><path d="M0 0l7 6 7-6" stroke="#fff" fill="none"/></svg>
<p class="f-text" style="left:611px;top:4127px">info@companyname.com</p>

<h4 class="f-head" style="left:888px">Links</h4>
<p class="f-text" style="left:888px;top:4043px;line-height:20.8px">Log in<br>Contact Us<br>FAQs<br>Press / Media<br>Partnership &amp; Licensing</p>

<div class="abs" style="left:0;top:4211px;width:1200px;height:1px;background:var(--line)"></div>
<p class="f-text" style="left:168px;top:4252px">© 2025 Brask Insurance.All Rights Reserved &nbsp;|&nbsp; Privacy Policy &nbsp;|&nbsp; Terms of Use</p>
<div class="social" style="left:854px"></div>
<div class="social" style="left:891px"></div>
<div class="social" style="left:928px"></div>
<div class="social" style="left:965px"></div>
<div class="social" style="left:1002px"></div>

</body>
</html>
```